Chemical Distribution Company Needs a Website

We need a website designed for an existing company based in Michigan. We have grown substantially since inception and we need our website to reflect this growth. It currently has a very mom and pop feel to it. What we do is ship chemicals in Drums, Totes, Bags, Bulk Tank Trucks, and rail from our warehouses in Toledo Oh, and Chicago il. This will be a site that strictly shows what we do and will not be E-commerced based. The final design should communicate a large business with NorthAmerican reach and worldwide sourcing capabilities.

Target Market(s)

What we sell are chemicals such as acids, solvents, oils, and salts all of which are used in the manufacturing process of various products from steel to car parts to paint to car wash soaps to food. We are trying to look like a large company that has stability and track record to go after all types of industries and manufacturers

Industry/Entity Type

It Company

Number of Pages Required

5+ page

Font styles to use
Serif
Sans Serif

Requirements
Must have
• Be Formatted for WIX as that is what we use to Host and Build. Unless you have a better idea. I would also like it to be viewed on a mobile platform which it is not now.
• Tabs for:
• Home Page (similar to "www.brindlemoor.com")
• Who we are- with subtabs for (Overview, Leadership, and Capabilities)
• Chemicals- (subtabs for (overview, Chemicals A-Z) Look at Brindlemoor.com
• Metal Working Lubricants (with a drop down identical to the products tab at "www.veltraslube.com"
• Contact- Very similar to www.quorvanta.com/contact/
• Need to have professional photos of Chemical Facilities, Bulk Tanks Trucks, Chemical Railcars, Storage Facilities filled with Drums and Totes, a Tank Farm.
Nice to have
• Want to have our site look like a combination of quorvanta.com, brindlemoor.com, and plimtoreach.com

```html
<!DOCTYPE html>
<html lang="en">
<head>
<meta charset="utf-8">
<title>Kestrel Chemicals</title>
<link href="https://fonts.googleapis.com/css2?family=Source+Sans+3:wght@400;600;700&display=swap" rel="stylesheet">
<style>
:root{
  --navy:#0f4a6e;
  --navy-deep:#1d3f5f;
  --blue:#2196e6;
  --text:#333a40;
  --bar:#1f3a30;
  --white:#ffffff;
  --mist:#dcecf6;
}
*{margin:0;padding:0;box-sizing:border-box}
html,body{width:1092px;height:1200px;overflow:hidden}
body{position:relative;font-family:"Source Sans 3",Arial,sans-serif;color:var(--text);background:var(--white)}
.topbar{position:absolute;left:0;top:0;width:1092px;height:55px;background:linear-gradient(90deg,#2a5560,#1e3a32 40%,#20402f)}
.social{position:absolute;left:68px;top:18px;display:flex;gap:18px}
.social span{width:18px;height:18px;border-radius:3px;background:var(--white);opacity:.9}
.phone{position:absolute;right:100px;top:16px;color:var(--white);font-size:16px;font-weight:600;display:flex;align-items:center;gap:10px}
.search{position:absolute;right:70px;top:18px}
.header{position:absolute;left:0;top:55px;width:1092px;height:102px;background:var(--white)}
.brand{position:absolute;left:68px;top:26px;display:flex;align-items:center;gap:12px}
.brand-dot{width:44px;height:44px;border-radius:50%;background:var(--navy)}
.brand-name{font-size:26px;font-weight:700;color:var(--navy);line-height:1;letter-spacing:.5px}
.brand-tag{font-size:6.5px;color:var(--blue);letter-spacing:.6px;margin-top:4px}
.nav{position:absolute;left:408px;top:44px;display:flex;gap:0;font-size:13px;font-weight:600;color:#222}
.nav a{color:inherit;text-decoration:none;padding:0 14px 7px}
.nav a.active{color:var(--blue);border-bottom:3px solid var(--blue)}
.hero{position:absolute;left:0;top:157px;width:1092px;height:347px;background:linear-gradient(100deg,#5f97ae 0%,#3f6f80 30%,#5c7468 55%,#2f4a3e 80%,#3b5a4c 100%)}
.hero-copy{position:absolute;left:0;top:105px;width:1092px;text-align:center;color:var(--white)}
.hero-copy h1{font-size:28px;font-weight:700;letter-spacing:.5px}
.hero-copy p{font-size:17px;font-weight:600;line-height:27px;margin-top:6px}
.btn{display:inline-block;margin-top:18px;background:var(--blue);color:var(--white);font-size:14px;font-weight:600;padding:11px 10px;text-decoration:none}
.features{position:absolute;left:0;top:504px;width:1092px;height:242px;background:linear-gradient(180deg,#fff 40%,var(--mist))}
.feature{position:absolute;top:-58px;width:280px;text-align:center}
.feature-icon{width:112px;height:112px;margin:0 auto;border-radius:50%;background:var(--navy-deep);border:5px solid var(--white);box-shadow:0 2px 6px rgba(0,0,0,.2);display:flex;align-items:center;justify-content:center}
.feature h2{margin-top:31px;font-size:15px;font-weight:600;color:var(--navy-deep);letter-spacing:.3px}
.feature p{font-size:13.5px;line-height:22px;margin-top:4px}
.divider-dot{position:absolute;left:521px;top:720px;width:50px;height:50px;border-radius:50%;background:var(--navy)}
.products-title{position:absolute;left:0;top:796px;width:1092px;text-align:center;font-size:21px;font-weight:700;color:var(--navy-deep);letter-spacing:.4px}
.products{position:absolute;left:68px;top:854px;display:flex;gap:25px}
.product{width:220px;text-align:center}
.product-photo{width:220px;height:149px;border-radius:9px}
.product span{display:block;margin-top:18px;font-size:12.5px;font-weight:600;color:var(--blue)}
.arrow{position:absolute;top:924px}
.footer{position:absolute;left:0;top:1065px;width:1092px;height:135px;background:var(--navy-deep)}
.footer-nav{position:absolute;left:69px;top:23px;font-size:11.5px;font-weight:600;color:var(--white);letter-spacing:.2px}
.footer-nav i{font-style:normal;margin:0 8px}
.footer-brand{position:absolute;left:69px;top:62px;display:flex;align-items:center;gap:8px}
.footer-brand .brand-dot{width:26px;height:26px;background:var(--blue)}
.footer-brand b{font-size:15px;color:var(--blue);font-weight:700}
.copyright{position:absolute;left:69px;top:100px;font-size:11px;color:var(--white)}
.badge{position:absolute;border-radius:6px;background:#2a5478}
</style>
</head>
<body>
<div class="topbar">
  <div class="social"><span></span><span></span><span></span><span></span><span></span></div>
  <div class="phone">
    <svg width="14" height="14" viewBox="0 0 24 24"><path fill="#fff" d="M6.6 10.8a15 15 0 0 0 6.6 6.6l2.2-2.2c.3-.3.7-.4 1-.2 1.1.4 2.3.6 3.6.6.6 0 1 .4 1 1V20c0 .6-.4 1-1 1A17 17 0 0 1 3 4c0-.6.4-1 1-1h3.5c.6 0 1 .4 1 1 0 1.3.2 2.5.6 3.6.1.3 0 .7-.2 1z"/></svg>
    <span>( 555 ) 010 4821 &nbsp;|</span>
  </div>
  <svg class="search" width="16" height="16" viewBox="0 0 24 24"><circle cx="10" cy="10" r="7" fill="none" stroke="#fff" stroke-width="3"/><line x1="15" y1="15" x2="22" y2="22" stroke="#fff" stroke-width="3"/></svg>
</div>

<header class="header">
  <div class="brand">
    <div class="brand-dot"></div>
    <div><div class="brand-name">KESTREL CHEMICALS</div><div class="brand-tag">SETTING THE INDUSTRY STANDARD FOR CUSTOMER SERVICE</div></div>
  </div>
  <nav class="nav">
    <a class="active" href="#">HOME</a><a href="#">WHO WE ARE</a><a href="#">CHEMICALS</a><a href="#">METAL WORKING LUBRICANTS</a><a href="#">CONTACT</a>
  </nav>
</header>

<section class="hero" role="img" aria-label="Gloved hand holding laboratory flasks of blue liquid in front of a chemistry chalkboard">
  <div class="hero-copy">
    <h1>LOREM IPSUM DOLOR SIT AMET</h1>
    <p>Vestibulum vel metus sit amet turpis bibendum tincidunt vel sit amet quam. Pellentesque<br>habitant morbi tristique senectus et netus et malesuada fames ac turpis egestas</p>
    <a class="btn" href="#">LEARN MORE</a>
  </div>
</section>

<section class="features">
  <div class="feature" style="left:78px">
    <div class="feature-icon"><svg width="34" height="36" viewBox="0 0 34 36"><circle cx="17" cy="10" r="9" fill="#fff"/><path d="M2 36v-6c0-6 5-10 15-10s15 4 15 10v6z" fill="#fff"/></svg></div>
    <h2>WHO WE ARE</h2>
    <p>Aliquam molestie, mi et imperdiet euismod,<br>dui purus auctor tellus, et interdum<br>acus lectus et ante..</p>
  </div>
  <div class="feature" style="left:406px">
    <div class="feature-icon"><svg width="40" height="56" viewBox="0 0 40 56"><path d="M14 14h12v14l11 22H3l11-22z" fill="none" stroke="#fff" stroke-width="3"/><path d="M8 41h24l4 8H4z" fill="#fff"/><rect x="12" y="11" width="16" height="3" fill="#fff"/><circle cx="18" cy="4" r="2.5" fill="#fff"/><circle cx="23" cy="8" r="1.5" fill="#fff"/></svg></div>
    <h2>CHEMICALS</h2>
    <p>Aliquam molestie, mi et imperdiet euismod,<br>dui purus auctor tellus, et interdum<br>acus lectus et ante..</p>
  </div>
  <div class="feature" style="left:734px">
    <div class="feature-icon"><svg width="46" height="40" viewBox="0 0 46 40"><g fill="#fff"><circle cx="16" cy="20" r="11"/><rect x="13" y="5" width="6" height="30"/><rect x="1" y="17" width="30" height="6"/><rect x="13" y="5" width="6" height="30" transform="rotate(45 16 20)"/><rect x="13" y="5" width="6" height="30" transform="rotate(-45 16 20)"/><circle cx="36" cy="10" r="6"/><circle cx="36" cy="30" r="6"/></g><circle cx="16" cy="20" r="4" fill="#1d3f5f"/><circle cx="36" cy="10" r="2" fill="#1d3f5f"/><circle cx="36" cy="30" r="2" fill="#1d3f5f"/></svg></div>
    <h2>METAL WORKING LUBRICANTS</h2>
    <p>Aliquam molestie, mi et imperdiet euismod,<br>dui purus auctor tellus, et interdum<br>acus lectus et ante..</p>
  </div>
</section>

<div class="divider-dot"></div>
<h2 class="products-title">OUR PRODUCTS</h2>

<svg class="arrow" style="left:36px" width="20" height="32" viewBox="0 0 20 32"><path d="M16 3 4 16l12 13" fill="none" stroke="#1d3f5f" stroke-width="5"/></svg>
<div class="products">
  <div class="product"><div class="product-photo" role="img" aria-label="Laboratory glassware and pipette in a chemical facility" style="background:linear-gradient(135deg,#e8eef2,#9fc3d4 60%,#4d8aa6)"></div><span>CHEMICAL FACILITIES</span></div>
  <div class="product"><div class="product-photo" role="img" aria-label="Bulk tank truck parked in front of storage tanks" style="background:linear-gradient(180deg,#5d8fc9,#c8d6e3 50%,#7b7f84)"></div><span>BULK TANKS TRUCKS</span></div>
  <div class="product"><div class="product-photo" role="img" aria-label="Chemical railcars at a rail yard" style="background:linear-gradient(180deg,#7a7460,#4a4438 50%,#6e665a)"></div><span>CHEMICAL RAILCARS</span></div>
  <div class="product"><div class="product-photo" role="img" aria-label="Spherical storage tanks with stairways at a tank farm" style="background:linear-gradient(135deg,#d8dbd8,#9ea7a2 50%,#4f8fbf)"></div><span>TANK FARM</span></div>
</div>
<svg class="arrow" style="left:1038px" width="20" height="32" viewBox="0 0 20 32"><path d="M4 3l12 13L4 29" fill="none" stroke="#1d3f5f" stroke-width="5"/></svg>

<footer class="footer">
  <div class="footer-nav">HOME<i>/</i>WHO WE ARE<i>/</i>CHEMICALS<i>/</i>METAL WORKING LUBRICANTS<i>/</i>CONTACT</div>
  <div class="footer-brand"><div class="brand-dot"></div><b>KESTREL CHEMICALS</b></div>
  <div class="copyright">Copyright © 2016. Company Name All Right Reserved</div>
  <div class="badge" style="left:736px;top:48px;width:134px;height:60px"></div>
  <div class="badge" style="left:900px;top:32px;width:118px;height:76px"></div>
</footer>
</body>
</html>
```